Plakat-Design für Tora-Unterricht einer Jüdischen Gemeinde
Zielgruppe
Wir sind die Jüdische Gemeinde.(synagogenverein Talbrück.
Wir organisieren einen Tora-Unterricht.
Zielgruppe sind Gemeindemitglieder(Männer und Frauen)die meisten aus der ehemaligen Sowjetunion, 50 Jahre aufwärts. Russischsprachig.
Die Plakate sollen in der Gemeinde hängen und so viele wie es geht ansprechen.
Aufgabenstellung
Plakat in russischer Sprache. Im folgenden steht der Text mit deutscher Übersetzung. Die Übersetzung dient nur zu Ihrer Information/Orientierung. Nur bei der Zeile mit Anführungsstrichen bleibt der deutsche Text:
Цикл лекций с раввином Элиэзер Розенфельд - Vortragsreihe von Rabbiner Elieser Rosenfeld
'Свет над морем-Licht über dem Meer'
По четвергам в 13.00 - donnerstags um 13:00 Uhr
С переводом на русский язык Светланы Мирошник - mit Übersetzung ins russische von Frau Swetlana Miroschnik
Приходите все! - Alle sind herzlich willkommen!
Вас ожидают увлека тельные уроки Торы а также интересные путешествия и экскурсии.- Euch erwarten spannende Tora Unterrichte und auch interessante Ausflüge und Besichtigung

```html
<!DOCTYPE html>
<html lang="ru">
<head>
<meta charset="utf-8">
<title>Цикл лекций с раввином Элиэзером Розенфельдом</title>
<link rel="stylesheet" href="https://fonts.googleapis.com/css2?family=Marck+Script&display=swap">
<style>
  :root {
    --teal: #1c8c84;
    --band: #4dbea3;
    --white: #ffffff;
    --peach: #f6b98c;
    --paper: #e9e4e2;
    --script: "Marck Script", cursive;
  }
  html, body {
    margin: 0;
    padding: 0;
    overflow: hidden;
    background: var(--teal);
  }
  .poster {
    position: relative;
    width: 848px;
    height: 1200px;
    background: var(--teal);
    color: var(--white);
    font-family: var(--script);
    overflow: hidden;
  }
  .headline {
    position: absolute;
    top: 28px;
    left: 0;
    width: 100%;
    margin: 0;
    text-align: center;
    font-weight: 400;
    font-size: 40px;
    line-height: 48px;
    letter-spacing: 2px;
    word-spacing: 8px;
  }
  .series-title {
    position: absolute;
    top: 146px;
    left: 0;
    width: 100%;
    margin: 0;
    text-align: center;
    font-size: 23px;
    letter-spacing: 1px;
    word-spacing: 5px;
  }
  .illustration {
    position: absolute;
    left: 83px;
    top: 190px;
    width: 680px;
    height: 708px;
    border-radius: 8px;
    background: radial-gradient(ellipse at 50% 45%, var(--paper) 0%, var(--paper) 18%, var(--peach) 40%, rgba(246,185,140,0.25) 62%, rgba(28,140,132,0) 78%);
  }
  .info-band {
    position: absolute;
    left: 30px;
    height: 41px;
    background: var(--band);
    font-size: 23px;
    line-height: 41px;
    padding: 0 8px;
    box-sizing: border-box;
    letter-spacing: 1px;
    word-spacing: 6px;
    white-space: nowrap;
  }
  .info-band--time { top: 927px; width: 273px; }
  .info-band--translation { top: 982px; width: 694px; font-size: 24px; }
  .teaser {
    position: absolute;
    top: 1040px;
    left: 0;
    width: 100%;
    margin: 0;
    text-align: center;
    font-size: 19px;
    line-height: 30px;
    letter-spacing: 1px;
    word-spacing: 6px;
  }
  .invitation {
    position: absolute;
    top: 1105px;
    left: 0;
    width: 100%;
    margin: 0;
    text-align: center;
    font-size: 56px;
    line-height: 72px;
    letter-spacing: 3px;
    word-spacing: 12px;
  }
</style>
</head>
<body>
  <main class="poster">
    <h1 class="headline">Цикл лекций с раввином<br>Элиэзером Розенфельдом</h1>
    <p class="series-title">‘Свет над морем - Licht über dem Meer’</p>

    <div class="illustration" role="img" aria-label="Иллюстрация: развёрнутый свиток Торы над раскрытыми ладонями, вокруг расходящиеся лучи"></div>

    <div class="info-band info-band--time">По четвергам в 13.00</div>
    <div class="info-band info-band--translation">С переводом на русский язык Светланы Мирошник</div>

    <p class="teaser">Вас ожидают увлекательные уроки Торы,<br>а также интересные путешествия и экскурсии.</p>

    <p class="invitation">Приходите все!</p>
  </main>
</body>
</html>
```